KJ Automation - Stationery and Identity.

Corporate Identity Design for the company, which includes Power Point presentations, Letterheads, business cards and mail signatures. We look for a simple design, but modern and elegant, that goes hand in hand with the technology that is the engine of the company.

Target Market(s)

Industrial Sector of Automation, Robotics and Process Control.

Industry/Entity Type

Automation

Colors

Designer to choose colors to be used in the design.

Requirements
Must have
• It must have an elegant, simple and clean design.

```html
<!DOCTYPE html>
<html lang="en">
<head>
<meta charset="utf-8">
<title>KJ Automation – Business Cards</title>
<link href="https://fonts.googleapis.com/css2?family=Exo+2:wght@400;600&display=swap" rel="stylesheet">
<style>
  :root {
    --page-bg: #e4e4e4;
    --card-bg: #ffffff;
    --brand-blue: #1a68a8;
    --brand-blue-light: #1fa3dc;
    --brand-grey: #9b9b9b;
    --text-grey: #555555;
    --text-dark: #444444;
  }
  * { box-sizing: border-box; margin: 0; padding: 0; }
  html, body { width: 1125px; height: 1200px; overflow: hidden; }
  body {
    background: var(--page-bg);
    font-family: "Exo 2", "Helvetica Neue", Arial, sans-serif;
    position: relative;
  }
  .card {
    position: absolute;
    left: 171px;
    width: 826px;
    height: 472px;
    background: var(--card-bg);
    box-shadow: 2px 3px 6px rgba(0,0,0,0.25);
  }
  .card--front { top: 106px; }
  .card--back { top: 639px; }

  .card__band {
    position: absolute;
    left: 0; bottom: 0;
    width: 826px; height: 15px;
    display: block;
  }

  .brand-mark {
    position: absolute;
    display: flex;
    align-items: center;
    gap: 12px;
    color: var(--brand-blue);
    font-weight: 600;
    white-space: nowrap;
  }
  .brand-mark__dot {
    border-radius: 50%;
    background: var(--brand-blue);
    flex: none;
  }
  .card--front .brand-mark {
    left: 140px; top: 170px;
    font-size: 30px;
  }
  .card--front .brand-mark__dot { width: 18px; height: 18px; }

  .divider {
    position: absolute;
    left: 392px; top: 124px;
    width: 14px; height: 172px;
  }

  .contact {
    position: absolute;
    left: 448px; top: 112px;
    color: var(--text-grey);
  }
  .contact__name {
    font-size: 33px;
    font-weight: 600;
    color: var(--brand-blue);
    letter-spacing: 0.5px;
    line-height: 1;
  }
  .contact__role {
    font-size: 19px;
    color: var(--brand-grey);
    margin-top: 4px;
    letter-spacing: 0.3px;
  }
  .contact__list { list-style: none; margin-top: 18px; }
  .contact__item { font-size: 19px; line-height: 26px; }
  .contact__item--small { font-size: 16px; }
  .contact__label { color: var(--brand-blue); font-weight: 600; }

  .address {
    position: absolute;
    left: 0; width: 100%;
    top: 362px;
    text-align: center;
    font-size: 17.5px;
    line-height: 26px;
    color: var(--text-grey);
  }

  .card--back .brand-mark {
    left: 50%; top: 186px;
    transform: translateX(-50%);
    font-size: 46px;
    gap: 16px;
  }
  .card--back .brand-mark__dot { width: 26px; height: 26px; }

  .website {
    position: absolute;
    left: 0; width: 100%;
    top: 396px;
    text-align: center;
    font-size: 17px;
    color: var(--text-dark);
    letter-spacing: 0.3px;
  }
</style>
</head>
<body>

<section class="card card--front" aria-label="Business card front">
  <div class="brand-mark">
    <span class="brand-mark__dot"></span>
    <span class="brand-mark__name">KJ Automation</span>
  </div>

  <svg class="divider" viewBox="0 0 14 172" aria-hidden="true">
    <line x1="7" y1="11" x2="7" y2="161" stroke="var(--brand-blue)" stroke-width="2.5"/>
    <circle cx="7" cy="7" r="5" fill="#fff" stroke="var(--brand-blue)" stroke-width="2.5"/>
    <circle cx="7" cy="165" r="5" fill="#fff" stroke="var(--brand-blue)" stroke-width="2.5"/>
  </svg>

  <div class="contact">
    <h1 class="contact__name">MATEO RUIZ</h1>
    <p class="contact__role">CEO/FOUNDER</p>
    <ul class="contact__list">
      <li class="contact__item"><span class="contact__label">P:</span> (+52) 33-4410-2285</li>
      <li class="contact__item"><span class="contact__label">C:</span> 33-5082-6649</li>
      <li class="contact__item contact__item--small">mruiz@kjautomation.com.mx</li>
      <li class="contact__item contact__item--small">www.kjautomation.com.mx</li>
    </ul>
  </div>

  <p class="address">Calle Roble No. 845, Col:Lomas Verdes C.P. 45210<br>Monte Azul, Jalisco, Mexico</p>

  <svg class="card__band" viewBox="0 0 826 15" preserveAspectRatio="none" aria-hidden="true">
    <defs>
      <linearGradient id="bandBlueFront" x1="0" x2="1" y1="0" y2="0">
        <stop offset="0" stop-color="#1762a4"/>
        <stop offset="0.6" stop-color="#1fa3dc"/>
        <stop offset="1" stop-color="#1a6fb0"/>
      </linearGradient>
    </defs>
    <polygon points="0,0 407,0 418,15 0,15" fill="url(#bandBlueFront)"/>
    <polygon points="414,0 826,0 826,15 425,15" fill="var(--brand-grey)"/>
  </svg>
</section>

<section class="card card--back" aria-label="Business card back">
  <div class="brand-mark">
    <span class="brand-mark__dot"></span>
    <span class="brand-mark__name">KJ Automation</span>
  </div>

  <p class="website">www.kjautomation.com.mx</p>

  <svg class="card__band" viewBox="0 0 826 15" preserveAspectRatio="none" aria-hidden="true">
    <defs>
      <linearGradient id="bandBlueBack" x1="0" x2="1" y1="0" y2="0">
        <stop offset="0" stop-color="#1762a4"/>
        <stop offset="0.6" stop-color="#1fa3dc"/>
        <stop offset="1" stop-color="#1a6fb0"/>
      </linearGradient>
    </defs>
    <polygon points="0,0 407,0 418,15 0,15" fill="url(#bandBlueBack)"/>
    <polygon points="414,0 826,0 826,15 425,15" fill="var(--brand-grey)"/>
  </svg>
</section>

</body>
</html>
```